On-Hold Advertising & Music Business needs logo design

Our umbrella name is Larkfen Sound Collective. Our main focus is providing custom on hold advertising and music (plays to callers on hold and businesses all over North America and Canada) The name of the company under this umbrella name is (and has been for 30 years) Quillmere Tones. We pioneered the on hold marketing/advertising industry in the mid 80's. The final design should communicate CREATIVE ADVERTISING & MUSIC SPECIFIC TO THE ON HOLD APPLICATION. In addition to ON HOLD MUSIC AND MESSAGING, The company offers IN-BUILDING (OVERHEAD) MUSIC, DIGITAL SIGNAGE, AND access to PROFESSIONAL VOICE TALENT including MULTILINGUAL TALENT. The card can be (but doesn't have to be) double sided. I would like to see something on the front side that screams ADVERTISING FOR THE ON HOLD ENVIRONMENT, and then perhaps the balance of what we offer on the back side? We create an audio portrait of a busiiness through messages that play to the business' callers while on hold. I hjave included our current logo but I am open to new logo ideas if it doesn't fit well on a card.

Target Market(s)

Businesses of all kinds, shapes and sizes. Owners, Managers, Representatives from the companies

Industry/Entity Type

Advertising

Contact Information for Business Card

We want the front side to scream CREATIVE on hold advertising and music. it should feature our logo and have our contact information on it. It should also have room for names of staff (one per card of course along with their title)

Colors

Designer to choose colors to be used in the design.

Requirements
Must have
• Nameof the company and it should be clear what we are leading with: CREATIVE ON HOLD ADVERTISING AND MUSIC. It should at least list (okay on the back) our other services: In-Building (overhead) Music, Digital Signage and access to Professional Voice Talent for IVR/Telephone prompts (multi-language talent too)
Should not have
• The card should not be crammed with information (or at least not look like it is)

```html
<!DOCTYPE html>
<html lang="en">
<head>
<meta charset="utf-8">
<title>Larkfen Sound Collective – Business Card</title>
<link href="https://fonts.googleapis.com/css2?family=Encode+Sans+Semi+Condensed:wght@400;500;700&display=swap" rel="stylesheet">
<style>
  :root {
    --bg: #eeeeee;
    --red: #d8222b;
    --red-light: #e2404a;
    --red-dark: #b8262f;
    --white: #ffffff;
    --ink: #555a60;
    --font: "Encode Sans Semi Condensed", sans-serif;
  }
  * { box-sizing: border-box; margin: 0; padding: 0; }
  html, body { width: 1200px; height: 1200px; overflow: hidden; background: var(--bg); }
  body { font-family: var(--font); position: relative; }

  .card {
    position: absolute;
    left: 170px;
    width: 860px;
    height: 491px;
    overflow: hidden;
    box-shadow: 0 6px 24px rgba(0,0,0,0.12);
  }
  .card--front { top: 70px; background: var(--white); }
  .card--back {
    top: 639px;
    background: linear-gradient(160deg, var(--red) 0%, var(--red-dark) 100%);
    color: var(--white);
  }

  .front-waves { position: absolute; inset: 0; width: 100%; height: 100%; }

  .person { position: absolute; top: 92px; left: 330px; }
  .person__name {
    color: var(--red);
    font-weight: 700;
    font-size: 40px;
    letter-spacing: 0.5px;
    line-height: 1;
    margin-left: 40px;
  }
  .person__role { color: var(--ink); font-size: 17px; margin-top: 6px; }
  .person__role .divider, .person__role .label { color: var(--red); }

  .brand {
    position: absolute;
    top: 200px;
    left: 340px;
    display: flex;
    align-items: center;
    gap: 14px;
  }
  .brand__dot { width: 46px; height: 46px; border-radius: 50%; background: var(--red); flex: none; }
  .brand__names { line-height: 1.25; }
  .brand__umbrella { color: var(--red); font-weight: 500; font-size: 19px; }
  .brand__company { color: var(--ink); font-weight: 500; font-size: 19px; }

  .contact {
    position: absolute;
    left: 44px;
    bottom: 44px;
    color: var(--white);
    font-size: 18px;
    line-height: 1.5;
  }
  .contact__rule { width: 330px; height: 1px; background: var(--white); margin-top: 8px; opacity: 0.9; }

  .services {
    position: absolute;
    right: 60px;
    top: 70px;
    text-align: right;
  }
  .services__title { font-size: 36px; font-weight: 400; margin-bottom: 26px; }
  .services__list { list-style: none; font-size: 24px; line-height: 1.7; }
</style>
</head>
<body>
  <section class="card card--front" aria-label="Business card front">
    <svg class="front-waves" viewBox="0 0 860 491" preserveAspectRatio="none" aria-hidden="true">
      <defs>
        <linearGradient id="band" x1="0" y1="0" x2="1" y2="1">
          <stop offset="0" stop-color="#d8222b"/>
          <stop offset="1" stop-color="#e2404a"/>
        </linearGradient>
      </defs>
      <path d="M0,95 C230,230 420,345 860,375" fill="none" stroke="#d8222b" stroke-width="9"/>
      <path d="M0,130 C240,300 470,405 860,420 L860,491 L0,491 Z" fill="url(#band)"/>
    </svg>

    <div class="person">
      <h1 class="person__name">JOHN DOE</h1>
      <p class="person__role">Director <span class="divider">|</span> <span class="label">T:</span> 1-234-567890</p>
    </div>

    <div class="brand">
      <span class="brand__dot" aria-hidden="true"></span>
      <div class="brand__names">
        <p class="brand__umbrella">Larkfen Sound Collective</p>
        <p class="brand__company">Quillmere Tones</p>
      </div>
    </div>

    <div class="contact">
      <p>Dummy city, Dummy Country Land</p>
      <p>www.companyname.com |john@companyname.com</p>
      <div class="contact__rule"></div>
    </div>
  </section>

  <section class="card card--back" aria-label="Business card back">
    <div class="services">
      <h2 class="services__title">Our Services</h2>
      <ul class="services__list">
        <li>In-Building (overhead) Music</li>
        <li>Digital Signage and access to Professional Voice</li>
        <li>Talent for IVR/Telephone prompts (multi-language talent too)</li>
      </ul>
    </div>
  </section>
</body>
</html>
```